Electronic Refurbishment Warehouse needs a Website

We are looking for a clean, professional looking design with iconic imagery. Our main point we want to get across is that we will help clients save time, and money, and provide outstanding quality. Our logo can be found in the uploads section. This site is used to impress clients that we have a pre-existing relationship with. This site will be available for the public but it will not be used to advertise to the public or to drive traffic to it. The color scheme we are looking to stay with is blue, but that is not to say that everything should be a shade of blue. Last note, see site map below.

Site Map:

Home
Company
a. company overview
b. CEO letter
Services
a. Remanufacture & Refurbishment Services
1. Consumer Electronics
2. Cellular Phones
b.Reverse Logistics Management
c.Warranty Repair & Field Services
d.Quality Control & Assurance
e.Warehousing & Distribution
Careers
Contact Us

Reason: We want to allocate more time for designers to do what they do best.

Target Market(s)

Phone and TV Retailers that may have units that need to be refurbished. Example Velorin, tallcart, qvo, etc.

Industry/Entity Type

Electronics

Requirements
Must have
• Home Page Slider.
Iconic imagery and navigation.
The ability to be put into the 960 Grid.

```html
<!DOCTYPE html>
<html lang="en">
<head>
<meta charset="utf-8">
<title>Novaro Group – Home</title>
<link rel="stylesheet" href="https://fonts.googleapis.com/css2?family=Open+Sans:wght@400;700&family=Arimo:wght@400;700&family=Roboto+Mono:wght@700&display=swap">
<style>
  :root {
    --header-top: #7aa7cc;
    --header-bottom: #5b93c2;
    --nav-active: #4f84b3;
    --page-bg: #ffffff;
    --band-gray: #f1f1f1;
    --rule: #d9d9d9;
    --heading: #333333;
    --body-text: #777777;
    --link: #1a73c0;
    --green-light: #b3e05c;
    --green-dark: #7cc12c;
    --footer-top: #86aac4;
    --footer-bottom: #5e9bcb;
    --white: #ffffff;
  }
  * { box-sizing: border-box; margin: 0; padding: 0; }
  html, body { width: 777px; height: 1200px; overflow: hidden; background: var(--page-bg); }
  body { position: relative; font-family: "Arimo", Arial, sans-serif; color: var(--body-text); }
  .abs { position: absolute; }

  .top-strip { left: 0; top: 0; width: 777px; height: 38px; background: var(--band-gray); }
  .site-header { left: 0; top: 38px; width: 777px; height: 46px;
    background: linear-gradient(var(--header-top), var(--header-bottom)); }
  .brand { left: 42px; top: 9px; display: flex; align-items: center; gap: 6px;
    color: var(--white); font-family: "Open Sans", sans-serif; font-size: 11px; font-weight: 400; letter-spacing: .3px; }
  .brand-mark { width: 26px; height: 26px; background: var(--white); opacity: .9; }
  .main-nav a { position: absolute; top: 0; height: 46px; line-height: 46px; color: var(--white);
    text-decoration: none; font-family: "Arimo", sans-serif; font-size: 12.5px; }
  .main-nav a.active { background: var(--nav-active); width: 81px; text-align: center; }

  .slider-band { left: 0; top: 84px; width: 777px; height: 272px; background: var(--band-gray);
    border-bottom: 2px solid var(--rule); }
  .slide-photo { left: 41px; top: 84px; width: 694px; height: 255px;
    background: linear-gradient(180deg, #c9c2b6 0%, #8a7a66 45%, #7a4a22 75%, #3a2a1e 100%); }
  .slide-caption { left: 0; top: 94px; width: 735px; height: 42px; background: rgba(255,255,255,.8); }
  .slide-caption h1 { position: absolute; left: 57px; top: 11px; font-family: "Arimo", sans-serif;
    font-weight: 400; font-size: 17px; color: var(--heading); }
  .slide-arrow { top: 191px; }

  .section-title { font-family: "Open Sans", sans-serif; font-weight: 700; font-size: 14px;
    color: var(--heading); letter-spacing: .3px; line-height: 15px; }
  .sidebar-rule { left: 206px; top: 421px; width: 1px; height: 477px; background: #ececec; }
  .news-item { left: 40px; width: 138px; font-family: "Open Sans", sans-serif; font-size: 9px;
    line-height: 14.6px; color: var(--heading); }
  .read-more { display: block; text-align: right; color: var(--link); margin-top: 1px; }

  .form-label { left: 41px; font-family: "Open Sans", sans-serif; font-size: 9.5px; color: var(--heading); }
  .form-field { left: 40px; width: 135px; border: 1px solid #d4d4d4; background: var(--white); }

  .service-art { top: 429px; height: 73px; }
  .service-name { top: 515px; width: 160px; text-align: center; font-family: "Open Sans", sans-serif;
    font-size: 11.5px; line-height: 14.6px; color: var(--link); }
  .content-rule { left: 235px; top: 570px; width: 497px; height: 1px;
    background: linear-gradient(90deg, #bbb, #eee); }
  .intro { left: 234px; width: 460px; font-size: 9.7px; line-height: 14.6px; }
  .value-text { top: 786px; width: 128px; font-size: 9.7px; line-height: 14.6px; }
  .value-label { font-family: "Roboto Mono", monospace; font-weight: 700; font-size: 16px; fill: #1f2a10; }

  .site-footer { left: 0; top: 956px; width: 777px; height: 244px;
    background: linear-gradient(var(--footer-top), var(--footer-bottom)); }
  .footer-col { top: 34px; color: var(--white); font-size: 8.5px; line-height: 14.6px; }
  .footer-col h3 { font-family: "Roboto Mono", monospace; font-size: 9.5px; font-weight: 700;
    letter-spacing: .3px; margin-bottom: 14px; }
  .footer-col li { list-style: none; }
</style>
</head>
<body>
  <div class="abs top-strip"></div>

  <header class="abs site-header">
    <div class="abs brand"><span class="brand-mark"></span><span>| NOVARO GROUP</span></div>
    <nav class="main-nav">
      <a style="left:402px">COMPANY</a>
      <a style="left:488px">SERVICES</a>
      <a class="active" style="left:564px">CAREERS</a>
      <a style="left:656px">CONTACT US</a>
    </nav>
  </header>

  <div class="abs slider-band"></div>
  <div class="abs slide-photo" role="img" aria-label="Photo of a boardroom with a long wooden table and black leather chairs"></div>
  <div class="abs slide-caption"><h1>MORE THAN A LOGISTICS COMPANY</h1></div>
  <svg class="abs slide-arrow" style="left:34px" width="34" height="50" viewBox="0 0 34 50"><polygon points="0,0 34,25 0,50" fill="#fff"/></svg>
  <svg class="abs slide-arrow" style="left:710px" width="34" height="50" viewBox="0 0 34 50"><polygon points="34,0 0,25 34,50" fill="#fff"/></svg>

  <aside>
    <h2 class="abs section-title" style="left:40px;top:396px">LATEST NEWS</h2>
    <div class="abs news-item" style="top:441px">Novaro, a large revers logistics services provider, is pleased to announce...<a class="read-more">Read More</a></div>
    <div class="abs news-item" style="top:524px">As more and more companies recognize their corporate responsibility...<a class="read-more">Read More</a></div>

    <h2 class="abs section-title" style="left:40px;top:634px;width:165px">LEARN HOW NOVARO CAN HELP</h2>
    <label class="abs form-label" style="top:679px">Name</label>
    <div class="abs form-field" style="top:695px;height:20px"></div>
    <label class="abs form-label" style="top:728px">Email</label>
    <div class="abs form-field" style="top:745px;height:20px"></div>
    <label class="abs form-label" style="top:780px">Phone</label>
    <div class="abs form-field" style="top:796px;height:20px"></div>
    <label class="abs form-label" style="top:830px">Comments</label>
    <div class="abs form-field" style="top:849px;height:86px"></div>
  </aside>
  <div class="abs sidebar-rule"></div>

  <main>
    <h2 class="abs section-title" style="left:235px;top:396px">SERVICES</h2>
    <div class="abs service-art" style="left:235px;width:121px;background:linear-gradient(180deg,#8aa0b4,#5d6f80)" role="img" aria-label="Illustration of a flat-screen TV and a mobile phone"></div>
    <div class="abs service-art" style="left:440px;width:90px;background:linear-gradient(180deg,#dce9f7,#a9c8ea)" role="img" aria-label="Illustration representing worldwide reverse logistics"></div>
    <div class="abs service-art" style="left:596px;width:145px;background:linear-gradient(180deg,#e9eef3,#c9d5e1)" role="img" aria-label="Illustration of warehouse shelving with a forklift"></div>
    <div class="abs service-name" style="left:217px">Remanufacture &amp;<br>Refurbishment Services</div>
    <div class="abs service-name" style="left:405px">Reverse Logistics<br>Management</div>
    <div class="abs service-name" style="left:587px">Warehousing &amp;<br>Distribution</div>
    <div class="abs content-rule"></div>

    <h2 class="abs section-title" style="left:234px;top:601px">WHAT WE DO</h2>
    <p class="abs intro" style="top:626px">We are the return / refurbish / repair specialists behind the brand.</p>
    <p class="abs intro" style="top:655px">For over 20 years, Novaro Group, Inc. has been serving the ever-growing consumer products industry.&nbsp; As a leading, large scale reverse logistics provider, we strive to deliver unsurpassed quality and support to manufacturers and their products.</p>

    <svg class="abs" style="left:248px;top:719px" width="466" height="54" viewBox="0 0 466 54">
      <defs>
        <linearGradient id="valueGreen" x1="0" y1="0" x2="0" y2="1">
          <stop offset="0" stop-color="var(--green-light)"/><stop offset="1" stop-color="var(--green-dark)"/>
        </linearGradient>
      </defs>
      <polygon points="0,8 140,8 140,0 168,27 140,54 140,46 0,46" fill="url(#valueGreen)"/>
      <polygon points="150,8 290,8 290,0 318,27 290,54 290,46 150,46 168,27" fill="url(#valueGreen)" stroke="#fff" stroke-width="1"/>
      <polygon points="300,8 438,8 438,0 466,27 438,54 438,46 300,46 318,27" fill="url(#valueGreen)" stroke="#fff" stroke-width="1"/>
      <text class="value-label" x="36" y="33">QUALITY</text>
      <text class="value-label" x="203" y="33">TIME</text>
      <text class="value-label" x="348" y="33">MONEY</text>
    </svg>
    <p class="abs value-text" style="left:256px">We strive to deliver unsurpassed quality and support to manufactures and their products.</p>
    <p class="abs value-text" style="left:408px">Take time to do what you do best, and let us handle what we do best.</p>
    <p class="abs value-text" style="left:557px">Save money by not paying in-house workers to do what we can do for less.</p>
  </main>

  <footer class="abs site-footer">
    <div class="abs footer-col" style="left:242px"><h3>ABOUT US</h3><ul><li>CEO Letter</li><li>Corporate Governance</li><li>Environmental Health</li><li>and Safety</li></ul></div>
    <div class="abs footer-col" style="left:364px"><h3>SERVICES</h3><ul><li>Remanufacture and</li><li>Refurbishment Services</li><li>Factory Repair Services</li><li>Reverse Logisics Management</li><li>Quality Control and</li><li>Assurance Services</li><li>Warehousing and Distribution</li></ul></div>
    <div class="abs footer-col" style="left:498px"><h3>CAREERS</h3><ul><li>Search Jobs</li></ul></div>
    <div class="abs footer-col" style="left:602px"><h3>LOCATIONS</h3><ul><li>New Jersey</li><li>Texas</li></ul></div>
  </footer>
</body>
</html>
```